Soho based IT support firm flyer.

We need a flyer to boost our business. We're a tech support firm based in Soho, London and provide helpdesk and call out support to SMEs in and around London.
They'll be two flyers with the same design. One is location specific and has the copy:
-
1 Month Free IT Support!
Based in Soho, we provide expert tech support for both Orbis and PCs.
We have monthly as well as pay-as-you-go plans to fit your business.
Call us now and we'll show you how we can save you up to 50% on your IT spend.
-None location based is-
1 Month Free IT Support!
We provide expert, professional tech support for both Orbis and PCs.
• Dedicated full time helpdesk
• Same day onsite visits
• Proactive support with monitoring
• 98% satisfaction score*
*taken from satisfaction survey sent out on closure of every case for Oct 2011 to Oct 2012
-
The location one needs to include a map with our location marked as postcode W9K 4TP.
I'm fine with royalty photos being used within a reasonable price. Please use PixQuarry.
Our site shows our brand best. Please keep as close to this as possible.
http://brisk-byte.example
Thanks for looking.

```html
<!DOCTYPE html>
<html lang="en">
<head>
<meta charset="utf-8">
<title>BriskByte IT Support Flyers</title>
<link rel="stylesheet" href="https://fonts.googleapis.com/css2?family=Cabin:wght@400;500&family=Nunito:wght@800;900&display=swap">
<style>
:root{
  --page:#ffffff;
  --paper:#fbfaf0;
  --brand-green:#c3d82e;
  --brand-orange:#f5a31d;
  --bullet-orange:#f0961a;
  --body-grey:#676767;
  --white:#ffffff;
  --map-tone:#e4e0d4;
}
*{margin:0;padding:0;box-sizing:border-box}
html,body{width:1200px;height:810px;overflow:hidden;background:var(--page)}
.sheet{position:relative;width:1200px;height:810px}
.flyer{position:absolute;top:33px;width:529px;height:734px;background:var(--paper);font-family:"Cabin",sans-serif;overflow:hidden}
.flyer--local{left:33px}
.flyer--general{left:617px}
.brand{position:absolute;left:26px;top:40px;display:flex;align-items:center;gap:10px;font-family:"Cabin",sans-serif;font-weight:500;font-size:46px;color:var(--brand-green);letter-spacing:-0.5px}
.brand__dot{width:16px;height:16px;border-radius:50%;background:var(--brand-green)}
.phone-tab{position:absolute;left:354px;top:0;width:142px;height:89px;background:var(--brand-orange);border-radius:0 0 4px 4px;color:var(--white);font-family:"Nunito",sans-serif;font-weight:800;font-size:21px;line-height:28px;text-align:center;padding-top:22px;letter-spacing:0.5px}
.headline{position:absolute;left:24px;top:110px;width:387px;height:50px;background:var(--brand-green);color:var(--white);font-family:"Nunito",sans-serif;font-weight:900;font-size:26px;line-height:50px;padding-left:34px;white-space:nowrap}
.intro{position:absolute;top:177px;color:var(--body-grey);font-size:19px;line-height:24px;white-space:nowrap}
.flyer--local .intro{left:34px}
.flyer--general .intro{left:26px;top:181px}
.intro p{margin-bottom:15px}
.perks{position:absolute;top:380px;list-style:none;color:var(--bullet-orange);font-size:19px}
.flyer--local .perks{left:32px}
.flyer--general .perks{left:32px}
.perks li{height:48.5px;line-height:28px}
.perks li::before{content:"\2022";margin-right:6px}
.photo{position:absolute;left:354px;width:135px}
.photo--cloud{top:356px;height:101px;background:linear-gradient(135deg,#e3e5e7,#9ea3a8)}
.photo--help{top:467px;height:98px;background:linear-gradient(135deg,#eceef0,#b8bcc0)}
.footnote{position:absolute;left:0;top:575px;width:529px;text-align:center;color:var(--bullet-orange);font-family:Arial,Helvetica,sans-serif;font-size:10.5px}
.contact-band{position:absolute;left:0;top:600px;width:529px;height:134px;background:var(--brand-orange);color:var(--white)}
.contact{position:absolute;left:0;top:12px;width:390px;text-align:center;font-family:"Nunito",sans-serif}
.contact__phone{font-weight:900;font-size:27px;line-height:32px;letter-spacing:0.5px}
.contact__email{font-weight:900;font-size:25px;line-height:38px}
.contact__address{font-weight:800;font-size:12.5px;line-height:17px;margin-top:1px}
.map{position:absolute;left:380px;top:20px;width:114px;height:80px;background:linear-gradient(160deg,var(--map-tone),#d6d2c4)}
</style>
</head>
<body>
<main class="sheet">

  <article class="flyer flyer--local">
    <div class="brand"><span>BriskByte</span><span class="brand__dot"></span></div>
    <div class="phone-tab">0203<br>555 0148</div>
    <h1 class="headline">1 Month Free IT Support!</h1>
    <div class="intro">
      <p>Based in Soho, we provide expert tech support<br>for both Orbis and PCs.</p>
      <p>We have monthly as well as pay-as-you-go plans<br>to fit your business.</p>
      <p>Call us now and we'll show you how we can<br>save you up to 50% on your IT spend.</p>
    </div>
    <ul class="perks">
      <li>Dedicated full time helpdesk</li>
      <li>Same day onsite visits</li>
      <li>Proactive support with monitoring</li>
      <li>98% satisfaction score*</li>
    </ul>
    <div class="photo photo--cloud" role="img" aria-label="Photo of a keyboard with a blue cloud key"></div>
    <div class="photo photo--help" role="img" aria-label="Photo of a keyboard with a red Help key"></div>
    <p class="footnote">*taken from satisfaction survey sent out on closure of every case for Oct 2011 to Oct 2012</p>
    <footer class="contact-band">
      <div class="contact">
        <div class="contact__phone">0203 555 0148</div>
        <div class="contact__email">info@brisk-byte.example</div>
        <div class="contact__address">12-14 Marlow House, Carver Street,<br>London W9K 4TP</div>
      </div>
      <div class="map" role="img" aria-label="Street map with the office location marked"></div>
    </footer>
  </article>

  <article class="flyer flyer--general">
    <div class="brand"><span>BriskByte</span><span class="brand__dot"></span></div>
    <div class="phone-tab">0203<br>555 0148</div>
    <h1 class="headline">1 Month Free IT Support!</h1>
    <div class="intro">
      <p>We provide expert, professional tech support for both<br>Orbis and PCs.</p>
      <p>We have monthly as well as pay-as-you-go plans to fit<br>your business.</p>
      <p>Call us now and we'll show you how we can save you<br>up to 50% on your IT spend.</p>
    </div>
    <ul class="perks">
      <li>Dedicated full time helpdesk</li>
      <li>Same day onsite visits</li>
      <li>Proactive support with monitoring</li>
      <li>98% satisfaction score*</li>
    </ul>
    <div class="photo photo--cloud" role="img" aria-label="Photo of a keyboard with a blue cloud key"></div>
    <div class="photo photo--help" role="img" aria-label="Photo of a keyboard with a red Help key"></div>
    <p class="footnote">*taken from satisfaction survey sent out on closure of every case for Oct 2011 to Oct 2012</p>
    <footer class="contact-band">
      <div class="contact">
        <div class="contact__phone">0203 555 0148</div>
        <div class="contact__email">info@brisk-byte.example</div>
        <div class="contact__address">12-14 Marlow House, Carver Street,<br>London W9K 4TP</div>
      </div>
      <div class="map" role="img" aria-label="Street map with the office location marked"></div>
    </footer>
  </article>

</main>
</body>
</html>
```